Residential technology services business card

Looking for a simple, catchy, slightly fun business card design.

We are a residential technology service provider (computer repair, tablet repair, training, etc). We are a fun, upbeat, yet professional company that is very skilled at our job.

I will upload our logo in a sec, thinking that it should be the only thing on the front side of the card, with maybe a punch line as well... maybe not. Maybe the punchline can find a place on the back. You be the judge.

Backside should be minimal in terms of information. I need two variations: one that will only have our website and phone and one that will also include a persons name (and position), personal e-mail and personal phone.

Well, you're the designer, figure out the best way to place all above mentioned items.

Colors are white, black, green (as in logo), plus whatever else you think needs adding (if any).

It must be clear to people what we do (provide computer services, tablet services)... without using generic pictures of computers and tablets, unless it 's something original.

We want something original! But do note that the card will be printed on standard size business card paper, so no funky shapes please.

Thanks!!!

Requirements
Must have
• Logo, website, phone.
2nd variation also must include space for persons name, personal phone and email.

```html
<!DOCTYPE html>
<html lang="en">
<head>
<meta charset="utf-8">
<title>ByteNest business cards</title>
<link href="https://fonts.googleapis.com/css2?family=Arimo:wght@400;700&display=swap" rel="stylesheet">
<style>
  :root {
    --backdrop: #7a4624;
    --card-white: #ffffff;
    --ink: #1e1c1c;
    --brand-green: #97c933;
    --stripe: #231f20;
  }
  html, body {
    margin: 0;
    width: 1134px;
    height: 1200px;
    overflow: hidden;
    background: var(--backdrop);
    font-family: "Arimo", Arial, sans-serif;
    color: var(--ink);
  }
  .canvas { position: relative; width: 1134px; height: 1200px; }

  .card {
    position: absolute;
    width: 580px;
    height: 340px;
    border-radius: 34px;
    overflow: hidden;
    background: var(--card-white);
    box-shadow: 0 6px 16px rgba(0,0,0,0.35);
  }
  .card--details { left: 90px; top: 240px; }
  .card--brand { left: 470px; top: 620px; }

  .details__green {
    position: absolute; left: 0; right: 0; top: 170px; bottom: 0;
    background: var(--brand-green);
  }
  .details__stripe {
    position: absolute; left: 0; right: 0; top: 158px; height: 12px;
    background: var(--stripe);
  }
  .details__website {
    position: absolute; right: 40px; top: 30px;
    font-size: 14px;
  }
  .details__company {
    position: absolute; left: 250px; top: 104px;
    font-size: 27px; font-weight: 700;
  }
  .logo-tile {
    position: absolute; left: 30px; top: 60px;
    width: 190px; height: 140px;
    background: var(--card-white);
    display: flex; align-items: center; justify-content: center; gap: 8px;
  }
  .wordmark {
    font-weight: 700; color: var(--ink); line-height: 1;
  }
  .wordmark__dot {
    width: 14px; height: 14px; background: var(--brand-green);
  }
  .logo-tile .wordmark { font-size: 32px; }

  .person {
    position: absolute; left: 180px; top: 238px; text-align: right; width: 140px;
  }
  .person__name { font-size: 22px; font-weight: 700; }
  .person__role { font-size: 19px; margin-top: 2px; }
  .contacts {
    position: absolute; left: 340px; top: 228px;
    font-size: 14px; line-height: 1.25;
  }

  .brand-logo {
    position: absolute; inset: 0;
    display: flex; align-items: center; justify-content: center; gap: 14px;
  }
  .brand-logo .wordmark { font-size: 58px; }
  .brand-logo .wordmark__dot { width: 22px; height: 22px; }
</style>
</head>
<body>
<main class="canvas">
  <section class="card card--details" aria-label="Card with contact details">
    <div class="details__green"></div>
    <div class="details__stripe"></div>
    <div class="details__website">www.bytenest.com</div>
    <div class="logo-tile">
      <span class="wordmark">ByteNest</span>
      <span class="wordmark__dot"></span>
    </div>
    <div class="details__company">Company Name</div>
    <div class="person">
      <div class="person__name">Abcd Xyz</div>
      <div class="person__role">Ceo</div>
    </div>
    <div class="contacts">
      <div>abcd@bytenest.com</div>
      <div>Phone(555)555-5555</div>
      <div>http://chirp.example/xyx</div>
    </div>
  </section>

  <section class="card card--brand" aria-label="Card with brand name">
    <div class="brand-logo">
      <span class="wordmark">ByteNest</span>
      <span class="wordmark__dot"></span>
    </div>
  </section>
</main>
</body>
</html>
```